Full Page Magazine Ad for Law Firm

Full Page Magazine Ad

The project is to design a full page ad to be place in Cannabis Harvest Quarterly magazine in the November 2017 edition.

Purpose of the ad is to promote Copperfield Ridge Law Group and not Martin Osgood from mo LAW ad.

About 20% of Copperfield Ridge Law Group’s current practice is marijuana related and it is looking grow that by illustrating in the ad that mo LAW is joining the firm.

Copperfield Ridge Law Group offers services in
• Tax Law
• Securities & Finance
• Business & Corporations
• Business Structuring
• Investments Funds & Management
• Rest Estate
• Outside General Counsel

mo LAW has offered services in:

• Marijuana regulation and compliance
• Buying and selling marijuana businesses
• Business & Corporations

Color palate should match Copperfield Ridge Law Group logo (blue) color with gray, black, white.

DO NOT want marijuana leaf images.
DO NOT include picture of Martin Osgood from mo LAW ad.

Documents provided:
Copperfield Ridge Law Group logo
Past mo LAW ad in magazine
Examples of competitor ads in same publication
Magazine spec sheet

Target Market(s)

The target of the ad is owners of larger marijuana retail stores and marijuana production/processing operations that need legal services.

Industry/Entity Type

Law Firm

Font styles to use
Other font styles liked:
• Should fit with CRLG logo.

Colors
3276b5

Requirements
Must have
• Copperfield Ridge Law Group is the Primary focus
• Use Copperfield Ridge Law Group address / contact information
• Ad must make clear that Copperfield Ridge Law Group is a Law Firm offering legal services to businesses.
Should not have
• DO NOT want marijuana leaf images.
• DO NOT include picture of Martin Osgood from mo LAW ad

```html
<!DOCTYPE html>
<html lang="en">
<head>
<meta charset="utf-8">
<title>Copperfield Ridge Law Group – Full Page Ad</title>
<link rel="stylesheet" href="https://fonts.googleapis.com/css2?family=Open+Sans:wght@300;400&display=swap">
<style>
  :root {
    --stage: #2b2b2b;
    --brand-blue: #3276b5;
    --banner-blue: #2a46a6;
    --hero-deep: #1e3a8a;
    --hero-mid: #2d4fb0;
    --accent-yellow: #ecec2c;
    --ink: #1e1e1e;
    --footer-black: #050505;
    --footer-gray: #8a8a8a;
    --white: #ffffff;
    --rule-blue: #4a86c8;
  }
  * { margin: 0; padding: 0; box-sizing: border-box; }
  html, body { width: 1200px; height: 1200px; overflow: hidden; background: var(--stage); }
  body { font-family: "Open Sans", sans-serif; position: relative; }

  .ad { position: absolute; left: 160px; top: 22px; width: 880px; height: 1156px; background: var(--white); overflow: hidden; }

  .hero { position: absolute; left: 0; top: 0; width: 880px; height: 510px; text-align: center; }
  .hero-photo { position: absolute; inset: 0;
    background: radial-gradient(ellipse at 55% 45%, #3a5cbc 0%, var(--hero-mid) 45%, var(--hero-deep) 100%); }
  .hero-line { position: absolute; left: 0; width: 100%; font-weight: 300; color: var(--white); white-space: nowrap; }
  .hero-line.accent { color: var(--accent-yellow); font-size: 58px; letter-spacing: 1px; font-weight: 400; }
  .hero-line.body { font-size: 35px; letter-spacing: 1px; }
  .l1 { top: 128px; } .l2 { top: 212px; } .l3 { top: 282px; } .l4 { top: 320px; }

  .hero-rule { position: absolute; left: 0; top: 510px; width: 880px; height: 7px; background: var(--rule-blue); }

  .services { position: absolute; left: 0; top: 517px; width: 880px; height: 484px; }
  .services-photo { position: absolute; inset: 0;
    background: linear-gradient(180deg, #d9dce2 0%, #e4e5e9 55%, #f6f6f7 80%, #ffffff 100%); }

  .banner { position: absolute; background: var(--banner-blue); color: var(--white); text-align: center;
    font-weight: 400; letter-spacing: 1px; display: flex; align-items: center; justify-content: center; white-space: nowrap; }
  .banner.firm { left: 48px; top: 32px; width: 800px; height: 54px; font-size: 25px; }
  .banner.partner { left: 117px; top: 230px; width: 645px; height: 53px; font-size: 29px; }

  .service-list { position: absolute; left: 20px; width: 840px; text-align: center; color: var(--ink);
    font-size: 24px; letter-spacing: 0.5px; }
  .service-list.firm { top: 102px; line-height: 36px; }
  .service-list.partner { top: 300px; line-height: 46px; }

  .firm-name { position: absolute; left: 0; top: 420px; width: 880px; text-align: center;
    color: var(--brand-blue); font-size: 31px; font-weight: 400; letter-spacing: 1px; }
  .firm-name small { font-size: 20px; }

  .footer { position: absolute; left: 0; top: 1001px; width: 880px; height: 155px; background: var(--footer-black); color: var(--white); }
  .footer-title { position: absolute; top: 12px; width: 100%; text-align: center; color: var(--footer-gray); font-size: 24px; letter-spacing: 1px; }
  .footer-row { position: absolute; left: 0; width: 100%; display: flex; justify-content: center; align-items: center; gap: 10px; font-size: 22px; letter-spacing: 0.5px; white-space: nowrap; }
  .footer-row.address { top: 56px; }
  .footer-row.contact { top: 106px; gap: 28px; }
  .contact-item { display: flex; align-items: center; gap: 12px; }
  .icon { width: 30px; height: 30px; fill: var(--white); flex: none; }
  .icon.globe { fill: none; stroke: var(--white); stroke-width: 1.6; }
</style>
</head>
<body>
<main class="ad">
  <section class="hero">
    <div class="hero-photo" role="img" aria-label="Blue-toned photograph of a judge's gavel on its sound block"></div>
    <p class="hero-line accent l1">wherever you need to be,</p>
    <p class="hero-line body l2">we deliver prompt personal service,</p>
    <p class="hero-line body l3">and strive to be efficent and cost-effective.</p>
    <p class="hero-line accent l4">we’ll get you there.</p>
  </section>
  <div class="hero-rule"></div>

  <section class="services">
    <div class="services-photo" role="img" aria-label="Faded photograph of a business meeting in a bright conference room"></div>
    <h2 class="banner firm">COPPERFIELD RIDGE LAW GROUP OFFERS SERVICES IN</h2>
    <p class="service-list firm">• Tax Law • Securities &amp; Finance &nbsp;• Business &amp;<br>Corporations &nbsp;• Business Structuring &nbsp;• Investments<br>Funds &amp; Management &nbsp;• Rest Estate • Outside General Counsel</p>
    <h2 class="banner partner">MO LAW HAS OFFERED SERVICES IN:</h2>
    <p class="service-list partner">• Marijuana regulation and compliance &nbsp;• Buying and selling<br>marijuana businesses &nbsp;• Business &amp; Corporations</p>
    <p class="firm-name">COPPERFIELD RIDGE LAW GROUP <small>PLLC</small></p>
  </section>

  <footer class="footer">
    <p class="footer-title">General Enquiries</p>
    <div class="footer-row address">
      <svg class="icon" viewBox="0 0 24 24" aria-hidden="true"><path d="M12 1a8 8 0 0 0-8 8c0 6 8 14 8 14s8-8 8-14a8 8 0 0 0-8-8zm0 11a3 3 0 1 1 0-6 3 3 0 0 1 0 6z"/></svg>
      <span>1250 Harbor Crest Avenue, Suite 410 Seattle, Washington 98121</span>
    </div>
    <div class="footer-row contact">
      <span class="contact-item">
        <svg class="icon" viewBox="0 0 24 24" aria-hidden="true"><path d="M6.6 10.8a15 15 0 0 0 6.6 6.6l2.2-2.2a1 1 0 0 1 1-.25 11.4 11.4 0 0 0 3.6.57 1 1 0 0 1 1 1V20a1 1 0 0 1-1 1A17 17 0 0 1 3 4a1 1 0 0 1 1-1h3.5a1 1 0 0 1 1 1c0 1.250.2 2.45.57 3.57a1 1 0 0 1-.25 1z"/></svg>
        (206) 555-0140
      </span>
      <span class="contact-item">
        <svg class="icon" viewBox="0 0 24 24" aria-hidden="true"><path d="M6 2h12v5H6zM3 8h18a1 1 0 0 1 1 1v7h-4v-3H6v3H2V9a1 1 0 0 1 1-1zm4 6h10v8H7z"/></svg>
        (206) 555-0148
      </span>
      <span class="contact-item">
        <svg class="icon globe" viewBox="0 0 24 24" aria-hidden="true"><circle cx="12" cy="12" r="10"/><ellipse cx="12" cy="12" rx="4.5" ry="10"/><path d="M2 12h20M4 6.5h16M4 17.5h16"/></svg>
        www.copperfieldridge-law.com
      </span>
    </div>
  </footer>
</main>
</body>
</html>
```